Corvath Partners is a boutique consultancy focused on CXO-level advisory on strategy, operations, and organization in the Consumer Packaged Goods and Retail sector.

Our typical clients are senior level executives (Typically SVP level or higher), who hire us to help solve strategic business challenges. Our consultants are typically charged out at very high rates (Typically $2,000 - $3,000 per day), therefore, our business cards need to convey a high end, classy, yet professional image, consistent with high value strategic consulting.

We would like to see designs and colors that convey excellence, competence, and growth.

Our name 'Corvath' is derived from the Native American name of Mt. McKinley, the highest peak in North America. We would like to have a logo on our business card, that is simple yet conveys the aspirational nature of what we offer, i.e enabling the achievement of high performance.

Boutique

Corvath Partners, LLC
4718 Brennock Avenue Northwest, Suite 640
Washington, District of Columbia, 20093
United States
Mobile: +1 202 555 0143
elira.voss@corvathpartnersllc.com

```html
<!DOCTYPE html>
<html lang="en">
<head>
<meta charset="utf-8">
<title>Corvath Partners — Business Card</title>
<link rel="stylesheet" href="https://fonts.googleapis.com/css2?family=Cinzel:wght@500&family=Michroma&display=swap">
<style>
  :root {
    --navy: #0d3a55;
    --orange: #ef4a1c;
    --ink: #3a3a3a;
    --rule: #9a9a9a;
    --paper: #ffffff;
    --backdrop: #e4e4e4;
  }
  html, body {
    margin: 0;
    width: 1200px;
    height: 900px;
    overflow: hidden;
    background: var(--backdrop);
  }
  .canvas {
    position: relative;
    width: 1200px;
    height: 900px;
  }
  .card {
    position: absolute;
    left: 75px;
    top: 150px;
    width: 1050px;
    height: 600px;
    background: var(--paper);
    overflow: hidden;
    box-shadow: 0 2px 10px rgba(0,0,0,0.12);
  }
  .card-band {
    position: absolute;
    inset: 0;
  }
  .band-url {
    font-family: "Michroma", sans-serif;
    font-size: 15px;
    letter-spacing: 3px;
    fill: #ffffff;
  }
  .wordmark {
    position: absolute;
    left: 0;
    width: 800px;
    top: 180px;
    text-align: center;
    margin: 0;
    font-family: "Cinzel", serif;
    font-weight: 500;
    font-size: 62px;
    letter-spacing: 1px;
    color: var(--navy);
  }
  .identity {
    position: absolute;
    right: 600px;
    top: 290px;
    text-align: right;
    font-family: "Michroma", sans-serif;
    font-variant: small-caps;
    color: var(--ink);
    letter-spacing: 1.5px;
  }
  .identity .person {
    color: var(--orange);
    font-size: 19px;
    margin: 0 0 6px;
  }
  .identity .role {
    font-size: 14px;
    margin: 0 0 28px;
  }
  .identity .address {
    font-size: 14px;
    line-height: 1.6;
    margin: 0;
    font-style: normal;
  }
  .divider {
    position: absolute;
    left: 470px;
    top: 270px;
    width: 1px;
    height: 150px;
    background: var(--rule);
  }
  .contacts {
    position: absolute;
    left: 490px;
    top: 262px;
    margin: 0;
    padding: 0;
    list-style: none;
    font-family: "Michroma", sans-serif;
    font-variant: small-caps;
    font-size: 13px;
    letter-spacing: 1px;
    color: var(--ink);
  }
  .contacts li {
    display: flex;
    align-items: center;
    gap: 9px;
    height: 22px;
  }
  .contacts li.gap-before { margin-top: 12px; }
  .contact-icon {
    width: 16px;
    height: 16px;
    flex: none;
  }
  .contact-icon circle { fill: var(--orange); }
  .contact-icon path, .contact-icon rect { fill: #ffffff; }
</style>
</head>
<body>
<main class="canvas">
  <section class="card" aria-label="Corvath Partners business card">
    <svg class="card-band" width="1050" height="600" viewBox="0 0 1050 600" aria-hidden="true">
      <path d="M10 600 Q700 526 1050 322 L1050 600 Z" fill="var(--orange)"/>
      <path d="M30 600 Q700 540 1050 340 L1050 600 Z" fill="var(--navy)"/>
      <path id="url-track" d="M300 588 Q760 540 1050 385" fill="none"/>
      <text class="band-url"><textPath href="#url-track" startOffset="60">www.corvathpartnersllc.com</textPath></text>
    </svg>

    <h1 class="wordmark">Corvath Partners</h1>

    <div class="identity">
      <p class="person">Elira Voss</p>
      <p class="role">Owner / C.E.O</p>
      <address class="address">Suite # 640, Brennock Ave,<br>DC 20093</address>
    </div>

    <div class="divider"></div>

    <ul class="contacts">
      <li>
        <svg class="contact-icon" viewBox="0 0 16 16"><circle cx="8" cy="8" r="8"/><path d="M5 4.5l1.6-.4 1 2-1 .8a5 5 0 0 0 2.5 2.5l.8-1 2 1-.4 1.6C8.5 11.5 4.5 7.5 5 4.5z"/></svg>
        +1 202 555 0143
      </li>
      <li>
        <svg class="contact-icon" viewBox="0 0 16 16"><circle cx="8" cy="8" r="8"/><rect x="5.5" y="3.5" width="5" height="9" rx="1"/></svg>
        +1 202 555 0178
      </li>
      <li>
        <svg class="contact-icon" viewBox="0 0 16 16"><circle cx="8" cy="8" r="8"/><rect x="4" y="6" width="8" height="5" rx="1"/><rect x="5.5" y="4" width="5" height="2"/></svg>
        +1 202 555 0192
      </li>
      <li class="gap-before">
        <svg class="contact-icon" viewBox="0 0 16 16"><circle cx="8" cy="8" r="8"/><rect x="4" y="5" width="8" height="6" rx="0.5"/><path d="M4 5l4 3.5L12 5z" fill="var(--orange)"/></svg>
        elira.voss@corvathpartnersllc.com
      </li>
      <li>
        <svg class="contact-icon" viewBox="0 0 16 16"><circle cx="8" cy="8" r="8"/><path d="M8 3.5a4.5 4.5 0 1 0 0 9a4.5 4.5 0 1 0 0-9zm0 1.2c.6.7 1 1.8 1.1 2.7H6.9c.1-.9.5-2 1.1-2.7zM6.9 8.6h2.2c-.1.9-.5 2-1.1 2.7-.6-.7-1-1.8-1.1-2.7z"/></svg>
        www.corvathpartnersllc.com
      </li>
    </ul>
  </section>
</main>
</body>
</html>
```